Hack my website! Blue Harbor needs a site

We hack stuff. No joke, that is what we do, but we are the good guys!

We do security consulting, specifically offensive security. The technical term is "Penetration Testing", but you probably know it as "hacking". Companies hire us to break in before the bad guys do. (I have a very cool job :) ).

I need a web site to describe our offerings and connect with clients.

I've included my business card and logo so you can understand what I'm looking for on the website and the color scheme.

Tag line:
Offensive Services from Offensive Minds

Target Market(s)

Medium to large businesses

Industry/Entity Type

Computer Security

Coding

Coded - Design and coding required

Number of Pages Required

2 page

Font styles to use
Sans Serif

Colors

Designer to choose colors to be used in the design.

Requirements
Must have
• Flat, clean, professional look
Nice to have
• Bonus for bootstrap. See the uploaded logo for the current colors. I'd really like this to look decent on a phone too.
Should not have
• 1. Black background
• 2. The business card is to show the colors and theme so far. Please, do NOT just slam that into the middle of the site since it doesn't make sense. It feels odd that I have to say that, but I've received multiple submissions where people have done this.

```html
<!DOCTYPE html>
<html lang="en">
<head>
<meta charset="utf-8">
<title>Blue Harbor — Offensive Security</title>
<link href="https://fonts.googleapis.com/css2?family=Oswald:wght@500;600&family=Roboto:ital,wght@0,400;0,500;1,400&family=Raleway:wght@500;600&display=swap" rel="stylesheet">
<style>
:root{
  --red:#d32027;
  --red-dark:#b71b21;
  --white:#ffffff;
  --ink:#1a1a1a;
  --hero-a:#0d3a44;
  --hero-b:#06161c;
  --dark:#151515;
  --navy-a:#0a1426;
  --navy-b:#060b16;
  --black:#0b0b0b;
}
*{box-sizing:border-box;margin:0;padding:0}
html,body{width:897px;height:1200px;overflow:hidden;background:var(--white)}
body{position:relative;font-family:'Roboto',Arial,sans-serif;color:var(--white)}
.site-header{position:absolute;left:0;top:0;width:897px;height:48px;background:var(--white);border-bottom:1px solid #e6e6e6}
.brand{position:absolute;left:132px;top:13px;display:flex;align-items:center;gap:8px;font-family:'Raleway',sans-serif;font-weight:600;font-size:17px;letter-spacing:3px;color:var(--red)}
.brand-dot{width:16px;height:16px;background:var(--red)}
.menu-toggle{position:absolute;left:746px;top:18px}
.hero{position:absolute;left:0;top:48px;width:897px;height:373px;background:radial-gradient(ellipse at 50% 45%,var(--hero-a),var(--hero-b) 75%)}
.hero-title{position:absolute;left:0;top:154px;width:897px;text-align:center;font-family:'Oswald',sans-serif;font-weight:600;font-style:italic;font-size:38px;letter-spacing:.3px}
.hero-lead{position:absolute;left:210px;top:204px;width:477px;text-align:center;font-style:italic;font-size:11.5px;line-height:14.6px}
.btn{position:absolute;left:387px;top:318px;width:123px;height:28px;background:var(--red);border-radius:2px;font-size:10.5px;font-weight:500;text-align:center;line-height:28px}
.badge{position:absolute;width:58px;height:58px;border-radius:50%;background:var(--white);left:419.5px;z-index:2}
.pivot{position:absolute;left:0;top:421px;width:897px;height:327px;background:var(--dark)}
.section-title{font-family:'Oswald',sans-serif;font-weight:600;font-style:italic;line-height:1.3}
.pivot .section-title{position:absolute;left:130px;top:67px;font-size:29px;line-height:34px}
.pivot-copy{position:absolute;left:132px;top:146px;width:305px;font-size:11px;line-height:15.5px}
.pivot-copy p+p{margin-top:15.5px}
.pivot-photo{position:absolute;left:450px;top:74px;width:315px;height:211px;border:4px solid var(--white);background:linear-gradient(120deg,#2a1f14,#5b3a1c 45%,#3a5a7a 75%,#1a2a3a)}
.rf{position:absolute;left:0;top:748px;width:897px;height:227px;background:linear-gradient(90deg,var(--navy-a),var(--navy-b) 60%,#1a1e28)}
.rf .section-title{position:absolute;left:0;top:64px;width:897px;text-align:center;font-size:36px}
.rf-copy{position:absolute;left:180px;top:122px;width:537px;text-align:center;font-size:11px;line-height:15.5px}
.site-footer{position:absolute;left:0;top:975px;width:897px;height:225px;background:var(--red)}
.footer-col{position:absolute;top:63px;font-family:'Raleway',sans-serif}
.footer-col h2{font-weight:500;font-size:20px;letter-spacing:.3px}
.contact{left:137px}
.contact ul{list-style:none;margin-top:10px}
.contact li{display:flex;align-items:center;gap:8px;font-family:'Roboto',sans-serif;font-size:15px;letter-spacing:.8px;height:26px}
.connect{left:351px}
.signup{display:flex;margin-top:11px}
.signup span{width:146px;height:31px;background:var(--white);color:#555;font-family:'Roboto',sans-serif;font-size:9.5px;line-height:31px;padding-left:9px}
.signup b{width:83px;height:31px;background:var(--black);font-family:'Raleway',sans-serif;font-weight:600;font-size:14px;line-height:31px;text-align:center}
.social{display:flex;gap:6px;margin-top:11px}
.social i{width:25px;height:25px;border:1.5px solid var(--white);border-radius:50%}
</style>
</head>
<body>
<header class="site-header">
  <div class="brand"><span class="brand-dot"></span>BLUE HARBOR</div>
  <svg class="menu-toggle" width="18" height="13" viewBox="0 0 18 13"><rect width="18" height="3" fill="#d32027"/><rect y="5" width="18" height="3" fill="#d32027"/><rect y="10" width="18" height="3" fill="#d32027"/></svg>
</header>

<section class="hero" role="img" aria-label="Hooded figure at a screen of streaming code">
  <h1 class="hero-title">Offensive Solutions from Offensive Minds</h1>
  <p class="hero-lead">Red Team Adversary Simulation - A goal based assessment where we attack just like a real world adversary. This includes external attacks and targeted phishing to demonstrate the real risk to your data.</p>
  <div class="btn">LEARN MORE</div>
</section>
<div class="badge" style="top:392px"></div>

<section class="pivot">
  <h2 class="section-title">Internal Pivot Assessment<br>Post Exploitation</h2>
  <div class="pivot-copy">
    <p>We start as a low privileged users and attempted to move through the network in an attempt to access the data the matters to you.</p>
    <p>This is a simulation of a rogue trusted insider or a compromised internal host. We determine your risk when the egg shell is cracked. Even a seemingly insignificant compromise can have big consequences, and our goal is to demonstrate this risk.</p>
  </div>
  <div class="pivot-photo" role="img" aria-label="Two engineers working at a desktop computer"></div>
</section>
<div class="badge" style="top:728px"></div>

<section class="rf" role="img" aria-label="Engineer reviewing code on monitors">
  <h2 class="section-title">Advanced Product, Hardware RF Testing</h2>
  <p class="rf-copy">This a highly customized assessment designed for you and your hardware. Depending on the product we will analyze custom RF protocols, reverse engineer OS and firmware, and analyze and fuzz network protocols. We have tested a range of products from toys to security products.</p>
</section>
<div class="badge" style="top:950px"></div>

<footer class="site-footer">
  <div class="footer-col contact">
    <h2>CONTACT</h2>
    <ul>
      <li><svg width="18" height="18" viewBox="0 0 24 24"><path d="M6.6 10.8a15 15 0 0 0 6.6 6.6l2.2-2.2a1 1 0 0 1 1-.25 11.4 11.4 0 0 0 3.6.57 1 1 0 0 1 1 1V20a1 1 0 0 1-1 1A17 17 0 0 1 3 4a1 1 0 0 1 1-1h3.5a1 1 0 0 1 1 1c0 1.25.2 2.45.57 3.6a1 1 0 0 1-.25 1z" fill="#fff"/></svg>555.014.2288</li>
      <li><svg width="18" height="18" viewBox="0 0 24 24"><circle cx="12" cy="12" r="4" fill="none" stroke="#fff" stroke-width="2.4"/><path d="M16 8v5a3 3 0 0 0 6 0v-1a10 10 0 1 0-4 8" fill="none" stroke="#fff" stroke-width="2.4"/></svg>sam@blueharbor.com</li>
      <li><svg width="18" height="18" viewBox="0 0 24 24" fill="none" stroke="#fff" stroke-width="1.8"><circle cx="12" cy="12" r="10"/><ellipse cx="12" cy="12" rx="4.5" ry="10"/><path d="M2 12h20M4 7h16M4 17h16"/></svg>blueharbor.com</li>
    </ul>
  </div>
  <div class="footer-col connect">
    <h2>STAY CONNECTED</h2>
    <div class="signup"><span>EMAIL</span><b>SIGN UP</b></div>
    <div class="social"><i></i><i></i><i></i><i></i></div>
  </div>
</footer>
</body>
</html>
```